Car wash line needed for the pylon inscription

We need a design template / print template for our advertising pylon so that the Plavex plates can be printed. The area to be printed is approx. 1.5m wide and approx. 2.70m high. We operate a car wash about 30m long. The washing rollers are equipped with scratch-free Nerva Plush foam material. Before the vehicle is put into the car wash it gets a manual high pressure pre-wash. There are four different washing programs: basic laundry € 7.50 (wheel cleaning, intensive washing, gloss drying comfort care € 10.50 (like base + active foam) special care € 13.00 (like comfort + glossy sealing with lotus wax) premium care € 15.50 (like special care + Underbody wash) The pylon is right on the driveway on a busy road, we want to achieve maximum attention with the pylons. It should not be too much content because the vehicles drive past it, due to an immediate gyro, the speed is however at about 40Km / h. Opening hours Mon-Fri. 08: 00-19: 00 Sat 07: 00-19: 00 The Plavex plates are red. The enclosed files show our pylon with a little appealing design proposal our advertising agency and the real local places. For the opinion you can see on the following link a clipvane video with a comparable car wash like ours, the washing process is well illustrated there. https://www.clipvane.net/watch?v=Rk4LmQw9ZpT Furthermore, we have a bonus card system who has washed our car 10 times gets the 11 laundry for free. From foam additives we use active foam from the comfort care and from the special care gets the vehicle lotus wax, which has the effect that the paint is sealed and keeps the shine longer. We need a design template / print template for our advertising pylon so that the Plavex plates can be printed. The area to be printed is approx. 1.5m wide and approx. 2.70m high. We operate a car wash about 30m long. The washing rollers are equipped with scratch-free Nerva Plush foam material. Before the vehicle is put into the car wash it gets a manual high pressure pre-wash. There are four different washing programs: basic laundry € 7.50 (wheel cleaning, intensive washing, gloss drying comfort care € 10.50 (like base + active foam) special care € 13.00 (like comfort + glossy sealing with lotus wax) premium care € 15.50 (like special care + Underbody wash) The pylon is right on the driveway on a busy road, we want to achieve maximum attention with the pylons. It should not be too much content because the vehicles drive past it, due to an immediate gyro, the speed is however at about 40Km / h. Opening hours Mon-Fri. 08: 00-19: 00 Sat 07: 00-19: 00 The Plavex plates are red. The enclosed files show our pylon with a little appealing design proposal our advertising agency and the real local places. For the opinion you can see on the following link a clipvane video with a comparable car wash like ours, the washing process is well illustrated there. https://www.clipvane.net/watch?v=Rk4LmQw9ZpT Furthermore, we have a bonus card system who has washed our car 10 times gets the 11 laundry for free. From foam additives we use active foam from the comfort care and from the special care gets the vehicle lotus wax, which has the effect that the paint is sealed and keeps the shine longer. We need a design template / print template for our advertising pylon so that the Plavex plates can be printed. The area to be printed is approx. 1.5m wide and approx. 2.70m high. We operate a car wash about 30m long. The washing rollers are equipped with scratch-free Nerva Plush foam material. Before the vehicle is put into the car wash it gets a manual high pressure pre-wash. There are four different washing programs: basic laundry € 7.50 (wheel cleaning, intensive washing, gloss drying comfort care € 10.50 (like base + active foam) special care € 13.00 (like comfort + glossy sealing with lotus wax) premium care € 15.50 (like special care + Underbody wash) The pylon is right on the driveway on a busy road, we want to achieve maximum attention with the pylons. It should not be too much content because the vehicles drive past it, due to an immediate gyro, the speed is however at about 40Km / h. Opening hours Mon-Fri. 08: 00-19: 00 Sat 07: 00-19: 00 The Plavex plates are red. The enclosed files show our pylon with a little appealing design proposal our advertising agency and the real local places. For the opinion you can see on the following link a clipvane video with a comparable car wash like ours, the washing process is well illustrated there. https://www.clipvane.net/watch?v=Rk4LmQw9ZpT Furthermore, we have a bonus card system who has washed our car 10 times gets the 11 laundry for free. From foam additives we use active foam from the comfort care and from the special care gets the vehicle lotus wax, which has the effect that the paint is sealed and keeps the shine longer. We need a design template / print template for our advertising pylon so that the Plavex plates can be printed. The area to be printed is approx. 1.5m wide and approx. 2.70m high. We operate a car wash about 30m long. The washing rollers are equipped with scratch-free Nerva Plush foam material. Before the vehicle is put into the car wash it gets a manual high pressure pre-wash. There are four different washing programs: basic laundry € 7.50 (wheel cleaning, intensive washing, gloss drying comfort care € 10.50 (like base + active foam) special care € 13.00 (like comfort + glossy sealing with lotus wax) premium care € 15.50 (like special care + Underbody wash) The pylon is right on the driveway on a busy road, we want to achieve maximum attention with the pylons. It should not be too much content because the vehicles drive past it, due to an immediate gyro, the speed is however at about 40Km / h. Opening hours Mon-Fri. 08: 00-19: 00 Sat 07: 00-19: 00 The Plavex plates are red. The enclosed files show our pylon with a little appealing design proposal our advertising agency and the real local places. For the opinion you can see on the following link a clipvane video with a comparable car wash like ours, the washing process is well illustrated there. https://www.clipvane.net/watch?v=Rk4LmQw9ZpT Furthermore, we have a bonus card system who has washed our car 10 times gets the 11 laundry for free. From foam additives we use active foam from the comfort care and from the special care gets the vehicle lotus wax, which has the effect that the paint is sealed and keeps the shine longer. We need a design template / print template for our advertising pylon so that the Plavex plates can be printed. The area to be printed is approx. 1.5m wide and approx. 2.70m high. We operate a car wash about 30m long. The washing rollers are equipped with scratch-free Nerva Plush foam material. Before the vehicle is put into the car wash it gets a manual high pressure pre-wash. There are four different washing programs: basic laundry € 7.50 (wheel cleaning, intensive washing, gloss drying comfort care € 10.50 (like base + active foam) special care € 13.00 (like comfort + glossy sealing with lotus wax) premium care € 15.50 (like special care + Underbody wash) The pylon is right on the driveway on a busy road, we want to achieve maximum attention with the pylons. It should not be too much content because the vehicles drive past it, due to an immediate gyro, the speed is however at about 40Km / h. Opening hours Mon-Fri. 08: 00-19: 00 Sat 07: 00-19: 00 The Plavex plates are red. The enclosed files show our pylon with a little appealing design proposal our advertising agency and the real local places. For the opinion you can see on the following link a clipvane video with a comparable car wash like ours, the washing process is well illustrated there. https://www.clipvane.net/watch?v=Rk4LmQw9ZpT Furthermore, we have a bonus card system who has washed our car 10 times gets the 11 laundry for free. From foam additives we use active foam from the comfort care and from the special care gets the vehicle lotus wax, which has the effect that the paint is sealed and keeps the shine longer. We need a design template / print template for our advertising pylon so that the Plavex plates can be printed. The area to be printed is approx. 1.5m wide and approx. 2.70m high. We operate a car wash about 30m long. The washing rollers are equipped with scratch-free Nerva Plush foam material. Before the vehicle is put into the car wash it gets a manual high pressure pre-wash. There are four different washing programs: basic laundry € 7.50 (wheel cleaning, intensive washing, gloss drying comfort care € 10.50 (like base + active foam) special care € 13.00 (like comfort + glossy sealing with lotus wax) premium care € 15.50 (like special care + Underbody wash) The pylon is right on the driveway on a busy road, we want to achieve maximum attention with the pylons. It should not be too much content because the vehicles drive past it, due to an immediate gyro, the speed is however at about 40Km / h. Opening hours Mon-Fri. 08: 00-19: 00 Sat 07: 00-19: 00 The Plavex plates are red. The enclosed files show our pylon with a little appealing design proposal our advertising agency and the real local places. For the opinion you can see on the following link a clipvane video with a comparable car wash like ours, the washing process is well illustrated there. https://www.clipvane.net/watch?v=Rk4LmQw9ZpT Furthermore, we have a bonus card system who has washed our car 10 times gets the 11 laundry for free. From foam additives we use active foam from the comfort care and from the special care gets the vehicle lotus wax, which has the effect that the paint is sealed and keeps the shine longer. We need a design template / print template for our advertising pylon so that the Plavex plates can be printed. The area to be printed is approx. 1.5m wide and approx. 2.70m high. We operate a car wash about 30m long. The washing rollers are equipped with scratch-free Nerva Plush foam material. Before the vehicle is put into the car wash it gets a manual high pressure pre-wash. There are four different washing programs: basic laundry € 7.50 (wheel cleaning, intensive washing, gloss drying comfort care € 10.50 (like base + active foam) special care € 13.00 (like comfort + glossy sealing with lotus wax) premium care € 15.50 (like special care + Underbody wash) The pylon is right on the driveway on a busy road, we want to achieve maximum attention with the pylons. It should not be too much content because the vehicles drive past it, due to an immediate gyro, the speed is however at about 40Km / h. Opening hours Mon-Fri. 08: 00-19: 00 Sat 07: 00-19: 00 The Plavex plates are red. The enclosed files show our pylon with a little appealing design proposal our advertising agency and the real local places. For the opinion you can see on the following link a clipvane video with a comparable car wash like ours, the washing process is well illustrated there. https://www.clipvane.net/watch?v=Rk4LmQw9ZpT Furthermore, we have a bonus card system who has washed our car 10 times gets the 11 laundry for free. From foam additives we use active foam from the comfort care and from the special care gets the vehicle lotus wax, which has the effect that the paint is sealed and keeps the shine longer. We need a design template / print template for our advertising pylon so that the Plavex plates can be printed. The area to be printed is approx. 1.5m wide and approx. 2.70m high. We operate a car wash about 30m long. The washing rollers are equipped with scratch-free Nerva Plush foam material. Before the vehicle is put into the car wash it gets a manual high pressure pre-wash. There are four different washing programs: basic laundry € 7.50 (wheel cleaning, intensive washing, gloss drying comfort care € 10.50 (like base + active foam) special care € 13.00 (like comfort + glossy sealing with lotus wax) premium care € 15.50 (like special care + Underbody wash) The pylon is right on the driveway on a busy road, we want to achieve maximum attention with the pylons. It should not be too much content because the vehicles drive past it, due to an immediate gyro, the speed is however at about 40Km / h. Opening hours Mon-Fri. 08: 00-19: 00 Sat 07: 00-19: 00 The Plavex plates are red. The enclosed files show our pylon with a little appealing design proposal our advertising agency and the real local places. For the opinion you can see on the following link a clipvane video with a comparable car wash like ours, the washing process is well illustrated there. https://www.clipvane.net/watch?v=Rk4LmQw9ZpT Furthermore, we have a bonus card system who has washed our car 10 times gets the 11 laundry for free. From foam additives we use active foam from the comfort care and from the special care gets the vehicle lotus wax, which has the effect that the paint is sealed and keeps the shine longer. We need a design template / print template for our advertising pylon so that the Plavex plates can be printed. The area to be printed is approx. 1.5m wide and approx. 2.70m high. We operate a car wash about 30m long. The washing rollers are equipped with scratch-free Nerva Plush foam material. Before the vehicle is put into the car wash it gets a manual high pressure pre-wash. There are four different washing programs: basic laundry € 7.50 (wheel cleaning, intensive washing, gloss drying comfort care € 10.50 (like base + active foam) special care € 13.00 (like comfort + glossy sealing with lotus wax) premium care € 15.50 (like special care + Underbody wash) The pylon is right on the driveway on a busy road, we want to achieve maximum attention with the pylons. It should not be too much content because the vehicles drive past it, due to an immediate gyro, the speed is however at about 40Km / h. Opening hours Mon-Fri. 08: 00-19: 00 Sat 07: 00-19: 00 The Plavex plates are red. The enclosed files show our pylon with a little appealing design proposal our advertising agency and the real local places. For the opinion you can see on the following link a clipvane video with a comparable car wash like ours, the washing process is well illustrated there. https://www.clipvane.net/watch?v=Rk4LmQw9ZpT Furthermore, we have a bonus card system who has washed our car 10 times gets the 11 laundry for free. From foam additives we use active foam from the comfort care and from the special care gets the vehicle lotus wax, which has the effect that the paint is sealed and keeps the shine longer.

Target Market(s)

germany

Colors

Designer to choose colors to be used in the design.

Requirements
Must have
• Print template for the print job in the accepted formats. Of course, the design must be in German
Nice to have
• Colors that attract attention, but are still serious. The content must be perceived when passing by and the customers must be aware of the car wash.
Should not have
• Kitschiges Design Too much content which takes longer to be read.

```html
<!DOCTYPE html>
<html lang="de">
<head>
<meta charset="utf-8">
<title>Autowäsche – Pylon</title>
<link rel="stylesheet" href="https://fonts.googleapis.com/css2?family=Archivo+Black&family=Roboto+Condensed:wght@700&family=Arimo:ital,wght@0,700;1,700&display=swap">
<style>
  :root {
    --crimson: #d4103f;
    --crimson-deep: #6a0012;
    --ribbon: #0a6fc2;
    --ribbon-fold: #0b3d86;
    --sky: #33b9f0;
    --sky-light: #c9f0ff;
    --sun: #ffd400;
    --ink: #000000;
    --paper: #ffffff;
    --badge-blue: #1378c8;
  }
  html, body {
    margin: 0;
    width: 960px;
    height: 1200px;
    overflow: hidden;
    background: var(--paper);
  }
  .pylon { display: block; width: 960px; height: 1200px; }
  .headline { font-family: "Archivo Black", sans-serif; fill: var(--crimson); }
  .ribbon-text { font-family: "Archivo Black", sans-serif; fill: var(--paper); }
  .claim { font-family: "Archivo Black", sans-serif; fill: var(--crimson); }
  .claim-condensed { font-family: "Roboto Condensed", sans-serif; font-weight: 700; fill: var(--crimson); }
  .badge-big { font-family: "Roboto Condensed", sans-serif; font-weight: 700; fill: var(--paper); }
  .badge-small { font-family: "Arimo", sans-serif; font-weight: 700; fill: var(--paper); }
  .footer-accent { font-family: "Arimo", sans-serif; font-style: italic; font-weight: 700; fill: var(--sun); }
  .footer-lead { font-family: "Archivo Black", sans-serif; font-style: italic; fill: var(--paper); }
  .footer-info { font-family: "Arimo", sans-serif; font-weight: 700; fill: var(--paper); }
  .footer-hours { font-family: "Arimo", sans-serif; font-style: italic; font-weight: 700; fill: var(--paper); }
</style>
</head>
<body>
<svg class="pylon" viewBox="0 0 1728 2160" xmlns="http://www.w3.org/2000/svg">
  <defs>
    <radialGradient id="sky-burst" cx="0.5" cy="0.45" r="0.7">
      <stop offset="0" stop-color="var(--sky-light)"/>
      <stop offset="0.55" stop-color="#7fd6fb"/>
      <stop offset="1" stop-color="var(--sky)"/>
    </radialGradient>
    <linearGradient id="footer-fill" x1="0" y1="0" x2="1" y2="1">
      <stop offset="0" stop-color="#8a0420"/>
      <stop offset="0.5" stop-color="#8f0626"/>
      <stop offset="1" stop-color="var(--crimson-deep)"/>
    </linearGradient>
  </defs>

  <!-- frame -->
  <rect class="frame" x="328" y="176" width="1069" height="1826" fill="var(--ink)"/>
  <rect class="panel" x="391" y="223" width="947" height="1722" fill="var(--paper)"/>

  <!-- headline -->
  <text class="headline" x="428" y="548" font-size="170" textLength="880" lengthAdjust="spacingAndGlyphs" transform="rotate(-11.3 428 548)">AUTOWÄSCHE</text>

  <!-- hero band -->
  <polygon points="391,574 1338,364 1338,374 391,584" fill="var(--ink)"/>
  <polygon points="391,590 1338,376 1338,396 391,612" fill="var(--sun)"/>
  <polygon role="img" aria-label="Illustration: glänzendes blaues Auto frontal vor Strahlenkranz mit Seifenblasen" points="391,612 1338,396 1338,926 391,1140" fill="url(#sky-burst)"/>
  <polygon points="391,1140 1338,926 1338,950 391,1164" fill="var(--sun)"/>

  <!-- ribbon 1 -->
  <polygon points="437,1245 466,1272 466,1238" fill="var(--ribbon-fold)"/>
  <polygon points="437,1185 1007,1048 988,1115 437,1245" fill="var(--ribbon)"/>
  <text class="ribbon-text" x="458" y="1225" font-size="44" textLength="520" lengthAdjust="spacingAndGlyphs" transform="rotate(-13.8 458 1225)">LACKSCHONEND MIT</text>
  <text class="claim" x="478" y="1308" font-size="82" textLength="520" lengthAdjust="spacingAndGlyphs" transform="rotate(-14.5 478 1308)">NERVA PLUSH</text>
  <text class="claim" x="476" y="1360" font-size="46" textLength="625" lengthAdjust="spacingAndGlyphs" transform="rotate(-15.5 476 1360)">SCHAUMSTOFF - WALZEN</text>

  <!-- ribbon 2 -->
  <polygon points="437,1460 466,1488 466,1452" fill="var(--ribbon-fold)"/>
  <polygon points="437,1398 1007,1265 988,1335 437,1460" fill="var(--ribbon)"/>
  <text class="ribbon-text" x="476" y="1442" font-size="52" textLength="285" lengthAdjust="spacingAndGlyphs" transform="rotate(-14 476 1442)">NUR HIER!</text>
  <text class="claim" x="476" y="1492" font-size="36" textLength="148" lengthAdjust="spacingAndGlyphs" transform="rotate(-14 476 1492)">WASCH</text>
  <text class="claim" x="478" y="1546" font-size="64" textLength="390" lengthAdjust="spacingAndGlyphs" transform="rotate(-16 478 1546)">GUTSCHEINE!</text>
  <text class="claim-condensed" x="478" y="1586" font-size="40" textLength="372" lengthAdjust="spacingAndGlyphs" transform="rotate(-16 478 1586)">Sparen Sie 10% für 10 x</text>

  <!-- ribbon 3 -->
  <polygon points="437,1680 466,1706 466,1672" fill="var(--ribbon-fold)"/>
  <polygon points="437,1618 1003,1482 988,1547 437,1680" fill="var(--ribbon)"/>
  <text class="ribbon-text" x="480" y="1652" font-size="46" textLength="500" lengthAdjust="spacingAndGlyphs" transform="rotate(-14 480 1652)">PERFEKTE WÄSCHE</text>
  <text class="claim" x="478" y="1714" font-size="54" textLength="590" lengthAdjust="spacingAndGlyphs" transform="rotate(-14 478 1714)">AUCH FÜR 1HR AUTO</text>

  <!-- badge -->
  <g class="badge">
    <circle cx="1168" cy="1378" r="118" fill="var(--crimson)" stroke="var(--crimson)" stroke-width="18" stroke-dasharray="14 9" stroke-linecap="round"/>
    <circle cx="1168" cy="1378" r="110" fill="var(--sun)"/>
    <circle cx="1168" cy="1378" r="100" fill="var(--badge-blue)"/>
    <text class="badge-big" x="1170" y="1336" font-size="36" text-anchor="middle">Ab xx.xx.</text>
    <text class="badge-big" x="1168" y="1368" font-size="32" text-anchor="middle">TESTEN</text>
    <text class="badge-small" x="1172" y="1392" font-size="21" text-anchor="middle">und gratis</text>
    <text class="badge-small" x="1172" y="1411" font-size="21" text-anchor="middle">einen</text>
    <text class="badge-small" x="1172" y="1431" font-size="21" text-anchor="middle">Cappuccino</text>
    <text class="badge-small" x="1172" y="1450" font-size="21" text-anchor="middle">genießen</text>
  </g>

  <!-- footer -->
  <polygon points="437,1750 1298,1545 1298,1945 437,1945" fill="url(#footer-fill)"/>
  <rect role="img" aria-label="Kleine Linienzeichnung eines Sportwagens mit Funkeln" x="975" y="1615" width="280" height="140" fill="#9a0c2e"/>
  <text class="footer-accent" x="1240" y="1808" font-size="38" text-anchor="end" textLength="415" lengthAdjust="spacingAndGlyphs">ETWAS BESONDERES</text>
  <text class="footer-lead" x="1240" y="1862" font-size="52" text-anchor="end" textLength="650" lengthAdjust="spacingAndGlyphs">ZUSÄTZLICH LOTUSWACHS</text>
  <text class="footer-info" x="868" y="1900" font-size="26" text-anchor="middle">ÖFFNUNGSZEITEN</text>
  <text class="footer-hours" x="472" y="1938" font-size="35" textLength="782" lengthAdjust="spacingAndGlyphs">Mo-Frei. 08:00-19:00 Uhr,  Sa 07:00-19:00 Uhr</text>
</svg>
</body>
</html>
```